Brook Outreach eCommerce (a-la-carte) Modern Edgy (Be Creative - Follow Brief)

//BROOK OUTREACH//
A-La-Carte style eCommerce site designed with pick and pay options. Full credit card payment gateway. Paypal offered, Google Pay, Apple Pay. (Open to suggestions: Wordpress, BigCommerce, Squarespace)

Designed to fit look and feel of logo. Warm, Inviting, Simple and Modern.

Pages (standard 5):
1. Main Page: Sample Cases/Photos, Hot Packages
2. About: Company statement, Staff bios, Our goals
3. Services: Place to list options, service offerings, prices of packages (ability to check out, pay, etc)
4. Portfolio: Place to showcase our work, testimonials, ratings
5. Contact: Contact form, Links to other platforms (Whatsapp, Telegram, Discord)

Links to Social Media, include ability to share throughout whole page.

***(See attached Logo - use for look and feel but feel free to be creative, only a suggestion)***

Target Market(s)

Business, Influencers, Brands

Industry/Entity Type

Branding & Marketing

Coding

Coded - Design and coding required

Number of Pages Required

5+ page

Colors
0054AA
0677BA
7BADD7
CADEEF
E8F1F8

Requirements
Must have
• Must be clean, easy to navigate, modern look and feel but warm and inviting
Nice to have
• Front Page - Main "HOT" offerings // About Page // Contact Page (Form - Links to Whatsapp, Telegram, Discord) // Services // Portfolio page -- Social Media Links
Should not have
• clutter.

```html
<!DOCTYPE html>
<html lang="en">
<head>
<meta charset="utf-8">
<title>Brook Outreach</title>
<link href="https://fonts.googleapis.com/css2?family=Poppins:wght@400;500;600;700&family=Roboto+Slab:wght@500;600&display=swap" rel="stylesheet">
<style>
:root{
  --navy:#0054AA;
  --blue:#0677BA;
  --sky:#7BADD7;
  --mist:#CADEEF;
  --pale:#E8F1F8;
  --ink:#1d2433;
  --muted:#5b6473;
  --white:#ffffff;
}
*{box-sizing:border-box;margin:0;padding:0}
html,body{width:710px;height:1200px;overflow:hidden}
body{position:relative;background:var(--pale);font-family:"Poppins",sans-serif;color:var(--ink)}
.abs{position:absolute}

/* header */
.brand{left:40px;top:36px;display:flex;align-items:center;gap:10px}
.brand-dot{width:34px;height:34px;border-radius:50%;background:var(--blue)}
.brand-name{font-family:"Roboto Slab",serif;font-weight:600;font-size:20px;color:var(--navy)}
.nav{left:250px;top:27px;display:flex;gap:20px;font-size:10px;font-weight:600;color:var(--navy);letter-spacing:.3px}
.cart{left:560px;top:24px}
.login{left:588px;top:22px;width:52px;height:24px;border:1.5px solid var(--navy);border-radius:3px;font-size:9px;font-weight:600;color:var(--navy);display:flex;align-items:center;justify-content:center;background:var(--white)}

/* hero */
.hero{left:70px;top:147px;width:570px;height:163px;background:var(--mist)}
.hero-title{left:20px;top:40px;font-family:"Roboto Slab",serif;font-weight:600;font-size:27px;line-height:36px;color:var(--blue);text-align:center;width:290px;letter-spacing:.5px}
.hero-art{left:350px;top:10px;width:210px;height:145px;border-radius:6px;background:linear-gradient(160deg,#dbe8f4,#b7d0e8)}

/* service cards */
.card{top:361px;width:170px;height:202px;background:var(--white);border-radius:6px;box-shadow:0 4px 14px rgba(0,84,170,.12);text-align:center}
.card-art{position:absolute;left:40px;top:14px;width:90px;height:64px;border-radius:6px}
.card-title{position:absolute;left:0;right:0;top:88px;font-size:13px;font-weight:700;letter-spacing:.4px}
.card-text{position:absolute;left:16px;right:16px;top:110px;font-size:9px;line-height:13px;color:var(--muted)}
.card-link{position:absolute;left:0;right:0;top:174px;font-size:9px;font-weight:600;text-decoration:underline}

/* testimonials */
.eyebrow{left:70px;top:654px;font-size:10px;font-weight:600;letter-spacing:.6px}
.t-heading{left:70px;top:680px;font-family:"Roboto Slab",serif;font-weight:500;font-size:29px;line-height:40px;color:var(--blue)}
.dots{left:70px;top:797px;display:flex;gap:14px}
.dots span{width:7px;height:7px;border-radius:50%;background:var(--mist)}
.dots span:first-child{background:var(--ink)}
.t-back{left:362px;top:770px;width:272px;height:70px;background:#f4f8fc;border-radius:6px;box-shadow:0 4px 14px rgba(0,84,170,.10)}
.t-back-name{left:30px;top:30px;font-size:10px;color:var(--muted);line-height:13px}
.t-card{left:322px;top:645px;width:278px;height:140px;background:var(--white);border-radius:6px;box-shadow:0 6px 18px rgba(0,84,170,.14)}
.avatar{left:-26px;top:-22px;width:50px;height:50px;border-radius:50%;background:linear-gradient(150deg,#7a8b9c,#3e4e60);border:3px solid var(--white)}
.quote{left:22px;top:18px;width:240px;font-size:10px;line-height:14px}
.person{left:22px;top:88px;font-size:10px;line-height:13px}
.person b{font-weight:600;display:block}
.person span{color:var(--muted);font-size:9px}
.stars{left:150px;top:102px;display:flex;gap:4px}
.arrows{left:650px;top:700px;display:flex;flex-direction:column;gap:22px}

/* footer */
.footer{left:0;top:950px;width:710px;height:250px;background:var(--sky);color:var(--white)}
.f-brand{left:70px;top:30px;font-family:"Poppins",sans-serif;font-weight:700;font-size:15px;letter-spacing:1px}
.f-label{font-size:9px;font-weight:600;letter-spacing:.6px}
.socials{left:70px;top:114px;display:flex;gap:12px}
.socials span{width:14px;height:14px;border-radius:50%;background:var(--white)}
.f-col{top:43px;font-size:10px;line-height:26px}
.f-col .f-label{line-height:14px;margin-bottom:7px}
.f-col a{display:block;color:var(--white);text-decoration:none;line-height:25px}
.subscribe{left:444px;top:77px;display:flex}
.subscribe .field{width:144px;height:31px;border:1px solid var(--white);border-radius:3px 0 0 3px;font-size:9px;padding:0 10px;display:flex;align-items:center;color:#eef5fb}
.subscribe .btn{width:47px;height:31px;background:var(--white);color:var(--navy);font-size:8px;font-weight:700;display:flex;align-items:center;justify-content:center;border-radius:0 3px 3px 0}
.f-rule{left:70px;top:178px;width:570px;height:1px;background:rgba(255,255,255,.6)}
.f-legal{left:470px;top:193px;display:flex;gap:28px;font-size:10px}
</style>
</head>
<body>

<header>
  <div class="abs brand"><span class="brand-dot"></span><span class="brand-name">Brook Outreach</span></div>
  <nav class="abs nav"><span>HOME</span><span>ABOUT</span><span>SERVICES</span><span>PORTFOLIO</span><span>CONTACT</span></nav>
  <svg class="abs cart" width="18" height="18" viewBox="0 0 24 24" fill="none" stroke="#0054AA" stroke-width="2"><path d="M3 4h3l2 11h11l2-8H7"/><circle cx="10" cy="19" r="1.5"/><circle cx="17" cy="19" r="1.5"/></svg>
  <div class="abs login">LOGIN</div>
</header>

<section class="abs hero">
  <h1 class="abs hero-title">Our Work Transforms Businesses</h1>
  <div class="abs hero-art" role="img" aria-label="Illustration of a desk with a hanging lamp, computer and plant"></div>
</section>

<section>
  <article class="abs card" style="left:70px">
    <div class="card-art" role="img" aria-label="Illustration of a creative team at work" style="background:linear-gradient(150deg,#f1c6d4,#8aa7e0)"></div>
    <h3 class="card-title">CREATIVE</h3>
    <p class="card-text">"Lorem Ipsum Dolor Sit Amet, Consectetur Adipiscing Elit. Donec Cursus Pulvinar Ultrices"</p>
    <a class="card-link">Read More</a>
  </article>
  <article class="abs card" style="left:271px">
    <div class="card-art" role="img" aria-label="Illustration of a developer with code panels" style="background:linear-gradient(150deg,#f4d24a,#3a3a44)"></div>
    <h3 class="card-title">DEVELOPMENT</h3>
    <p class="card-text">"Lorem Ipsum Dolor Sit Amet, Consectetur Adipiscing Elit. Donec Cursus Pulvinar Ultrices"</p>
    <a class="card-link">Read More</a>
  </article>
  <article class="abs card" style="left:472px">
    <div class="card-art" role="img" aria-label="Illustration of a marketer presenting growth charts" style="background:linear-gradient(150deg,#9fb3ef,#e7a98f)"></div>
    <h3 class="card-title">MARKETING</h3>
    <p class="card-text">"Lorem Ipsum Dolor Sit Amet, Consectetur Adipiscing Elit. Donec Cursus Pulvinar Ultrices"</p>
    <a class="card-link">Read More</a>
  </article>
</section>

<section>
  <div class="abs eyebrow">TESTIMONIALS</div>
  <h2 class="abs t-heading">What People<br>Say About Us</h2>
  <div class="abs dots"><span></span><span></span><span></span></div>

  <div class="abs t-back">
    <div class="abs t-back-name">Owen Partridge<br><span style="font-size:8px">CEO of Larkspur Freight</span></div>
  </div>

  <div class="abs t-card">
    <div class="abs avatar" role="img" aria-label="Client portrait"></div>
    <p class="abs quote">"Lorem Ipsum Dolor Sit Amet, Consectetur Adipiscing Elit. Donec Cursus Pulvinar Ultrices"</p>
    <div class="abs person"><b>Mara Lindqvist</b><span>Social Art</span></div>
    <div class="abs stars">
      <svg width="12" height="12" viewBox="0 0 24 24"><path fill="#f5b921" d="M12 2l3 7 7 .6-5.3 4.7L18.4 22 12 18l-6.4 4 1.7-7.7L2 9.6 9 9z"/></svg>
      <svg width="12" height="12" viewBox="0 0 24 24"><path fill="#f5b921" d="M12 2l3 7 7 .6-5.3 4.7L18.4 22 12 18l-6.4 4 1.7-7.7L2 9.6 9 9z"/></svg>
      <svg width="12" height="12" viewBox="0 0 24 24"><path fill="#f5b921" d="M12 2l3 7 7 .6-5.3 4.7L18.4 22 12 18l-6.4 4 1.7-7.7L2 9.6 9 9z"/></svg>
      <svg width="12" height="12" viewBox="0 0 24 24"><path fill="#f5b921" d="M12 2l3 7 7 .6-5.3 4.7L18.4 22 12 18l-6.4 4 1.7-7.7L2 9.6 9 9z"/></svg>
      <svg width="12" height="12" viewBox="0 0 24 24"><path fill="#d8dee6" d="M12 2l3 7 7 .6-5.3 4.7L18.4 22 12 18l-6.4 4 1.7-7.7L2 9.6 9 9z"/></svg>
    </div>
  </div>

  <div class="abs arrows">
    <svg width="16" height="16" viewBox="0 0 24 24" fill="none" stroke="#9aa3ae" stroke-width="2.5"><path d="M5 15l7-7 7 7"/></svg>
    <svg width="16" height="16" viewBox="0 0 24 24" fill="none" stroke="#9aa3ae" stroke-width="2.5"><path d="M5 9l7 7 7-7"/></svg>
  </div>
</section>

<footer class="abs footer">
  <div class="abs f-brand">BROOK OUTREACH</div>
  <div class="abs f-label" style="left:70px;top:92px">SOCIAL MEDIA</div>
  <div class="abs socials"><span></span><span></span><span></span></div>

  <div class="abs f-col" style="left:250px">
    <div class="f-label">SHOP</div>
    <a>Products</a><a>Overview</a><a>Pricing</a><a>Releases</a>
  </div>
  <div class="abs f-col" style="left:343px">
    <div class="f-label">COMPANY</div>
    <a>About Us</a><a>Contact</a><a>News</a><a>Support</a>
  </div>
  <div class="abs f-label" style="left:444px;top:43px">STAY UP TO DATE</div>
  <div class="abs subscribe"><div class="field">Enter Your Email</div><div class="btn">SUBMIT</div></div>

  <div class="abs f-rule"></div>
  <div class="abs f-legal"><span>Terms</span><span>Privacy</span><span>Cookies</span></div>
</footer>

</body>
</html>
```